Website Templates Design Project

BrawnLoop Template Websites
Creative Brief

BrawnLoop Gyms
The growth of BrawnLoop Gyms (or boxes, as they are called by members) is an amazing world-wide phenomenon. More than 3,400 gyms ranging from “garage gyms” to massive retail locations have opened in recent years. The philosophy for workouts at the gym is built around is “constantly varied (if not random), high intensity, functional movement". Each gym does what is called a WOD, or Workout of the Day. Workouts are typically short—20 minutes or less—and intense, demanding all-out physical exertion.
The growth of the gyms, mainly in the United States, has generally come from military veterans, police officers and fireman. However, BrawnLoop box owners are mostly trainers and not necessarily skilled in operating or marketing a business. Our company is launching a new platform for boxes to purchase inexpensive template websites and other marketing materials.
The Need
Most BrawnLoop box owners have launched with basic WordPress websites. We see an opportunity to provide more dynamic and professional websites, using a template and content management system. We aim to offer multiple template designs (not WordPress) for box owners. The platform that we are using can be found at www.sitekitpreview7.com. We are looking for graphic designs that will fit this platform.
A big part of the BrawnLoop philosophy is built around an Internet-based community. Therefore, our website templates should allow for a robust blog that allows for posting of pictures and video by members and the box owner.
The Designs
We strongly encourage designers to review other BrawnLoop websites for design ideas and functionality (good and bad).
We are looking for cutting-edge designs. One person on our team said, “these sites need to be so good that they sweat!” Obviously, imagery that portrays working out and muscles will be attractive to box owners. Many of the graphics for BrawnLoop sites use particularly masculine images like diamond plate and steel. The designs should be contemporary and at first glance you show know that this is a BrawnLoop website.
Rotating images and video windows are good, just nothing that will require long load times.

Images and Logos
Please don’t pirate logos ad images from BrawnLoop sites without permission. For your design submissions, feel free to develop generic logos and names for BrawnLoop Gyms. If you use and stock photography, please indicate whether you have permission to use or where permission can be obtained.

The navigation for a basic website design (and your designs) should include:
Home (with WOD blog dominating body of page)
About Us
Store
Membership Info (with link to store)
Directions
Contact Us

Target Market(s)

18-35, athletic types, male and female

Industry/Entity Type

Marketing

Requirements
Must have
• Navigation "buttons":

About Us
Store
Directions
Contact Us

```html
<!DOCTYPE html>
<html lang="en">
<head>
<meta charset="utf-8">
<title>BrawnLoop Gyms</title>
<link href="https://fonts.googleapis.com/css2?family=Alfa+Slab+One&family=Sancreek&family=Rokkitt:wght@500&family=Roboto:wght@300;400&display=swap" rel="stylesheet">
<style>
:root{
  --page:#e4e1d4;
  --paper:#f8f3e6;
  --rust:#c4561e;
  --ink:#1d1b18;
  --bar:#2a2826;
  --maroon:#7d0b0b;
  --crimson:#8e1f1f;
  --tan:#d8b27a;
  --cream:#efe1c0;
  --muted:#8a857c;
  --field:#d6d1c0;
  --star:#6f6253;
  --rule:#cfc9bb;
  --social:#c4784e;
}
*{margin:0;padding:0;box-sizing:border-box}
html,body{width:1200px;height:1097px;overflow:hidden}
body{background:var(--page);font-family:'Roboto',sans-serif;position:relative}
.page{position:absolute;left:98px;top:0;width:1001px;height:1029px;background:var(--paper)}
.abs{position:absolute}
.header-photo{left:640px;top:0;width:361px;height:130px;background:linear-gradient(90deg,rgba(248,243,230,1),rgba(214,208,196,.7) 60%,rgba(200,194,182,.8))}
.brand-name{left:0;width:1001px;top:22px;text-align:center;font-family:'Roboto',sans-serif;font-weight:400;font-size:58px;line-height:66px;color:var(--ink)}
.tagline{left:0;width:1001px;top:100px;text-align:center;font-size:13px;letter-spacing:12px;color:var(--muted)}
.nav{left:11px;top:132px;width:979px;height:48px;background:var(--bar);display:flex;align-items:center;justify-content:space-around;padding:0 12px}
.nav a{font-family:'Sancreek',serif;color:#fff;text-decoration:none;font-size:22px;letter-spacing:.5px}
.nav .star{color:var(--rust);font-size:22px}
.hero{left:11px;top:204px;width:648px;height:306px;background:var(--bar);padding:9px}
.hero-photo{width:100%;height:100%;background:radial-gradient(ellipse at 38% 35%,#a0684a 0,#6a3e2a 22%,#140c08 48%,#000 70%)}
.hero-caption{left:9px;top:128px;width:375px;height:125px;background:rgba(140,24,24,.85);color:#fff;font-family:'Sancreek',serif;text-align:center}
.hero-caption .small{font-size:38px;line-height:46px;margin-top:4px}
.hero-caption .big{font-size:70px;line-height:72px}
.promo{left:684px;top:204px;width:306px;height:306px;background:var(--bar);padding:9px}
.promo-card{width:100%;height:100%;background:var(--cream);text-align:center;border:1px solid #c9b58e}
.promo .get{font-family:'Alfa Slab One',serif;color:var(--maroon);font-size:66px;line-height:66px;margin-top:34px}
.promo .premium{font-family:'Alfa Slab One',serif;color:var(--tan);font-size:26px;line-height:28px}
.promo .membership{font-family:'Alfa Slab One',serif;color:var(--ink);font-size:30px;line-height:36px}
.promo .cta{display:inline-block;margin-top:8px;width:224px;height:60px;line-height:62px;background:var(--crimson);border-radius:4px;color:#fff;font-family:'Alfa Slab One',serif;font-size:28px}
.col-head{border-top:1px solid var(--rule);border-bottom:1px solid var(--rule);height:55px;font-family:'Sancreek',serif;font-weight:400;font-size:36px;line-height:55px;padding-left:3px}
.welcome{left:11px;top:535px;width:276px}
.welcome .col-head{color:var(--ink)}
.welcome p{font-size:12px;line-height:15px;color:var(--muted);text-align:justify;margin-top:18px;font-weight:300}
.welcome p+p{margin-top:15px}
.why{left:347px;top:535px;width:277px}
.why .col-head{color:#c0ad96}
.why ul{list-style:none;margin-top:12px}
.why li{font-family:'Rokkitt',serif;font-size:18px;color:var(--ink);height:41px;line-height:30px;padding-left:10px}
.why li:last-child{margin-top:6px}
.why li span{color:var(--star);margin-right:14px}
.contact{left:684px;top:535px;width:306px}
.contact .col-head{color:var(--maroon);text-align:center}
.field-row{display:flex;margin-top:18px}
.field-row label{width:102px;font-family:'Sancreek',serif;font-size:18px;color:#6a6660;padding:10px 0 0 5px}
.field-row .box{width:204px;height:38px;background:var(--field);border-radius:2px}
.field-row + .field-row{margin-top:18px}
.field-row .box.msg{height:95px}
.field-row.msg-row{margin-top:16px}
.field-row.msg-row label{padding-top:0}
.submit{left:847px;top:829px;width:119px;height:43px;background:var(--maroon);border:3px solid #3a0606;color:#f3d9a3;font-family:'Sancreek',serif;font-size:22px;text-align:center;line-height:36px}
.footer-band{left:11px;top:898px;width:979px;height:9px;background:linear-gradient(90deg,#8a857a,#5e5a53 40%,#3d3a35 70%,#6a655c)}
.footer-nav{left:15px;top:939px;font-size:11px;color:var(--ink);white-space:nowrap}
.footer-nav a{color:var(--maroon);text-decoration:none}
.footer-nav .sep{margin:0 8px}
.social{left:657px;top:930px;display:flex;gap:11px}
.social span{width:31px;height:31px;border-radius:50%;background:var(--social);display:block}
.copyright{right:16px;top:940px;font-size:10.5px;color:#3a3733;white-space:nowrap}
</style>
</head>
<body>
<div class="page">
  <div class="abs header-photo" role="img" aria-label="Faded photo of an athlete's shoulder and arm"></div>
  <div class="abs brand-name">BrawnLoop Gyms</div>
  <div class="abs tagline">CATCH WORD OF BRAWN LOOP GYMS</div>

  <nav class="abs nav">
    <a href="#">HOME</a><span class="star">★</span>
    <a href="#">ABOUT US</a><span class="star">★</span>
    <a href="#">STORE</a><span class="star">★</span>
    <a href="#">MEMBERSHIP INFO</a><span class="star">★</span>
    <a href="#">DIRECTIONS</a><span class="star">★</span>
    <a href="#">CONTACT US</a>
  </nav>

  <section class="abs hero">
    <div class="hero-photo" role="img" aria-label="Photo of a muscular man curling a dumbbell against a black background"></div>
    <div class="abs hero-caption">
      <div class="small">HAVE YOUR DAILY</div>
      <div class="big">WORK OUT</div>
    </div>
  </section>

  <aside class="abs promo">
    <div class="promo-card">
      <div class="get">GET</div>
      <div class="premium">PREMIUM</div>
      <div class="membership">MEMBERSHIP</div>
      <a class="cta">CLICK HERE</a>
    </div>
  </aside>

  <section class="abs welcome">
    <h2 class="col-head">WELCOME TO</h2>
    <p>Lorem ipsum dolor sit amet, consectetur adipiscing elit. Integer non lacus neque. Nunc quis orci sed sem rhoncus facilisis.</p>
    <p>Sed magna sem, facilisis eget consequat sit amet, gravida ut eros. Aenean viverra, enim condimentum commodo placerat, nulla elit ornare diam, a vestibulum urna justo sed velit.</p>
    <p>In mollis, sem quis posuere lacinia, dolor erat lacinia turpis, at mattis nibh sem non eros. Duis iaculis placerat augue, quis sodales felis commodo ac.</p>
  </section>

  <section class="abs why">
    <h2 class="col-head">WHY US?</h2>
    <ul>
      <li><span>★</span>Lorem Ipsum dolor sit amet</li>
      <li><span>★</span>Consectetur adipiscing elit</li>
      <li><span>★</span>Facilisis eget consequat</li>
      <li><span>★</span>Quis sodales felis commodo</li>
      <li><span>★</span>Sed magna sem</li>
    </ul>
  </section>

  <section class="abs contact">
    <h2 class="col-head">QUICK CONTACT</h2>
    <div class="field-row"><label>NAME:</label><div class="box"></div></div>
    <div class="field-row"><label>EMAIL:</label><div class="box"></div></div>
    <div class="field-row msg-row"><label>MESSAGE:</label><div class="box msg"></div></div>
  </section>
  <div class="abs submit">SUBMIT</div>

  <div class="abs footer-band"></div>
  <div class="abs footer-nav">
    <a href="#">Home</a><span class="sep">|</span><a href="#">About Us</a><span class="sep">|</span><a href="#">Store</a><span class="sep">|</span><a href="#">Membership Info</a><span class="sep">|</span><a href="#">Directions</a><span class="sep">|</span><a href="#">Contact Us</a>
  </div>
  <div class="abs social"><span></span><span></span><span></span></div>
  <div class="abs copyright">© 2012. BrawnLoopGyms. All Rights Reserved</div>
</div>
</body>
</html>
```